Vexel Business Cards

We need a new look business cvard to refelect our new look website www.vexel-example.com.au
We’re Vexel, a team of town planning and traffic and transport engineering specialists located in Melbourne.

Vexel is a company that is structured, articulate, dynamic, progressive, accurate and adaptable.
Our key messages are:
1. We make your life easier by doing what we do best
2. We tell you what you need to know not what you want to hear
3. Polished and professional but not afraid to show some personality

we would like a bold new look that is polished and professional but not afraid to show a bit of personality

Target Market(s)

Vexel’s diverse client base consists of architecture practices, builders, developers, local government and the legal fraternity.

Industry/Entity Type

Town

Requirements
Must have
• must use our logo and have the following information

Joel Harcastle
Director

Vexel Consultants Pty Ltd
Fernhollow first floor
Tamber Street
Larkmoor VX 3999 Norvania
+61 03 9555 0187
mail@vexel-example.com.au
www.vexel-example.com.au
Nice to have
• We would like to see the logo used or the colours of the logo used.

```html
<!DOCTYPE html>
<html lang="en">
<head>
<meta charset="utf-8">
<title>Vexel Business Cards</title>
<link rel="stylesheet" href="https://fonts.googleapis.com/css2?family=Open+Sans:wght@400;700&display=swap">
<style>
  :root {
    --backdrop: #d9d6d2;
    --card: #f1f1f1;
    --ink: #2b2b2b;
    --wordmark: #4f5861;
    --green: #3cb54a;
    --shadow: rgba(0, 0, 0, 0.22);
  }
  * { box-sizing: border-box; margin: 0; padding: 0; }
  html, body {
    width: 1200px;
    height: 960px;
    overflow: hidden;
    background: var(--backdrop);
    font-family: "Open Sans", Arial, sans-serif;
    color: var(--ink);
  }
  .card-set {
    position: relative;
    width: 1200px;
    height: 960px;
    display: flex;
    align-items: center;
    justify-content: center;
    gap: 60px;
  }
  .card {
    position: relative;
    width: 520px;
    height: 297px;
    background: var(--card);
    box-shadow: 0 6px 18px var(--shadow);
  }

  /* Contact side */
  .card--contact { padding: 28px 34px; }
  .brand {
    display: flex;
    align-items: center;
    gap: 10px;
    margin-bottom: 14px;
  }
  .brand__name {
    font-size: 26px;
    font-weight: 400;
    color: var(--wordmark);
    line-height: 1;
  }
  .brand__square {
    width: 22px;
    height: 22px;
    background: var(--green);
  }
  .person__name { font-size: 13px; font-weight: 700; line-height: 1.35; }
  .person__title { font-size: 13px; line-height: 1.35; margin-bottom: 14px; }
  .address { font-style: normal; font-size: 13px; line-height: 1.35; }
  .address__company { font-weight: 700; }
  .contacts {
    position: absolute;
    right: 34px;
    bottom: 26px;
    list-style: none;
    text-align: right;
    font-size: 13px;
    line-height: 1.35;
  }
  .contacts b { font-weight: 700; }

  /* Brand side */
  .card--brand {
    display: flex;
    align-items: center;
    justify-content: center;
    gap: 22px;
  }
  .card--brand .brand__name {
    font-size: 96px;
    letter-spacing: 1px;
  }
  .card--brand .brand__square {
    width: 56px;
    height: 56px;
  }
</style>
</head>
<body>
  <main class="card-set">
    <section class="card card--contact" aria-label="Contact side">
      <div class="brand">
        <span class="brand__name">vexel</span>
        <span class="brand__square"></span>
      </div>
      <p class="person__name">Joel Harcastle</p>
      <p class="person__title">Director</p>
      <address class="address">
        <span class="address__company">Vexel Consultants Pty Ltd</span><br>
        Fernhollow first floor<br>
        Tamber Street<br>
        Larkmoor VX 3999 Norvania
      </address>
      <ul class="contacts">
        <li><b>tel:</b> +61 03 9555 0187</li>
        <li><b>web:</b> www.vexel-example.com.au</li>
        <li><b>email:</b> mail@vexel-example.com.au</li>
      </ul>
    </section>

    <section class="card card--brand" aria-label="Brand side">
      <span class="brand__name">vexel</span>
      <span class="brand__square"></span>
    </section>
  </main>
</body>
</html>
```